KLT Business cards

I currently have a logo that was designed by a mark hive designer. I would like this to be added to the business card.

We are an innovative new start-up business offering finance solutions to the car dealership market in the UK. So our clients are quiet traditional, so are cards need to fit in, but at the same time show we are a modern online business.

Finance

```html
<!DOCTYPE html>
<html lang="en">
<head>
<meta charset="utf-8">
<title>KLT Business Cards</title>
<link rel="stylesheet" href="https://fonts.googleapis.com/css2?family=Mulish:wght@400;800&display=swap">
<style>
  :root {
    --navy: #1f2f5c;
    --navy-mid: #3c4a74;
    --steel: #8d95ad;
    --silver: #d7dae3;
    --silver-light: #eef0f4;
    --paper: #ffffff;
    --ink: #1f2f5c;
    --muted: #9aa0ac;
    --canvas: #f4f5f7;
  }
  * { box-sizing: border-box; margin: 0; padding: 0; }
  html, body { width: 1200px; height: 1000px; overflow: hidden; background: var(--canvas); }
  body { font-family: "Mulish", sans-serif; color: var(--ink); position: relative; }

  .card {
    position: absolute; top: 326px; width: 540px; height: 349px;
    overflow: hidden; box-shadow: 0 8px 24px rgba(20, 30, 60, 0.18);
  }
  .card--contact { left: 40px; background: var(--paper); }
  .card--brand {
    left: 620px;
    background: linear-gradient(180deg, var(--navy) 0%, var(--navy-mid) 35%, var(--steel) 70%, var(--silver) 100%);
  }

  /* contact side */
  .contact__panel {
    position: absolute; left: 0; top: 0; width: 236px; height: 100%;
    background: linear-gradient(90deg, var(--navy) 0%, var(--navy-mid) 55%, var(--steel) 100%);
  }
  .contact__divider {
    position: absolute; left: 236px; top: 0; width: 12px; height: 100%;
    background: linear-gradient(90deg, var(--silver) 0%, var(--steel) 100%);
  }
  .contact__edge {
    position: absolute; right: 0; top: 0; width: 34px; height: 100%;
    background: linear-gradient(90deg, var(--silver-light) 0%, var(--steel) 45%, var(--navy) 100%);
  }
  .ring-decor {
    position: absolute; left: 0; top: 0; width: 120px; height: 100%;
    background: linear-gradient(90deg, rgba(20, 30, 70, 0.35), rgba(20, 30, 70, 0));
  }
  .brand-lockup { position: absolute; display: flex; align-items: center; gap: 12px; }
  .brand-lockup__mark { width: 54px; height: 54px; border-radius: 50%; border: 3px solid currentColor; flex: none; }
  .brand-lockup__name { font-weight: 800; font-size: 30px; letter-spacing: 1px; }
  .contact__panel .brand-lockup { left: 100px; top: 38px; color: var(--paper); }
  .company-name { position: absolute; line-height: 1; }
  .company-name span { display: block; font-size: 30px; font-weight: 400; }
  .company-name span.company-name__strong { font-weight: 800; }
  .contact__panel .company-name { left: 100px; top: 112px; color: var(--paper); }

  .person { position: absolute; left: 274px; top: 40px; }
  .person__name { font-size: 24px; font-weight: 800; color: var(--ink); }
  .person__role { font-size: 18px; color: var(--muted); margin-top: 10px; }
  .details { position: absolute; left: 274px; top: 160px; list-style: none; }
  .details li { display: flex; align-items: center; gap: 9px; font-size: 13px; margin-bottom: 11px; color: var(--ink); }
  .details__icon { width: 14px; height: 14px; border-radius: 50%; background: var(--ink); flex: none; display: flex; align-items: center; justify-content: center; }

  /* brand side */
  .hub-decor {
    position: absolute; left: 170px; top: 40px; width: 420px; height: 420px; border-radius: 50%;
    background: radial-gradient(circle at 40% 35%, var(--silver-light) 0%, var(--silver) 45%, var(--steel) 100%);
    box-shadow: inset 0 0 0 10px rgba(255,255,255,0.35);
  }
  .card--brand .ring-decor { width: 100%; height: 90px; background: linear-gradient(180deg, rgba(20,30,70,0.35), rgba(20,30,70,0)); }
  .card--brand .brand-lockup { left: 200px; top: 120px; color: var(--navy); }
  .card--brand .company-name { left: 290px; top: 118px; color: var(--navy); }
  .tagline { position: absolute; left: 290px; top: 232px; font-size: 17px; color: var(--navy); }
</style>
</head>
<body>
  <section class="card card--contact">
    <div class="contact__panel">
      <div class="ring-decor" role="img" aria-label="Faint overlapping ring pattern"></div>
      <div class="brand-lockup">
        <span class="brand-lockup__mark"></span>
        <span class="brand-lockup__name">KLT</span>
      </div>
      <p class="company-name">
        <span>Kerb</span>
        <span>Lane</span>
        <span class="company-name__strong">Traders</span>
      </p>
    </div>
    <div class="contact__divider"></div>
    <div class="person">
      <p class="person__name">Tom Harlow</p>
      <p class="person__role">Founder</p>
    </div>
    <ul class="details">
      <li>
        <span class="details__icon">
          <svg width="8" height="8" viewBox="0 0 24 24"><path fill="#fff" d="M6.6 10.8a15.1 15.1 0 0 0 6.6 6.6l2.2-2.2c.3-.3.7-.4 1-.2 1.1.4 2.3.6 3.6.6.6 0 1 .4 1 1V20c0 .6-.4 1-1 1A17 17 0 0 1 3 4c0-.6.4-1 1-1h3.5c.6 0 1 .4 1 1 0 1.3.2 2.5.6 3.6.1.3 0 .7-.2 1z"/></svg>
        </span>07700 900123
      </li>
      <li><span class="details__icon"></span>tom.harlow_klt</li>
      <li><span class="details__icon"></span>www.kerblanetraders.com</li>
      <li><span class="details__icon"></span>tom.harlow@kerblanetraders.com</li>
    </ul>
    <div class="contact__edge"></div>
  </section>

  <section class="card card--brand">
    <div class="ring-decor" role="img" aria-label="Faint overlapping ring pattern"></div>
    <div class="hub-decor" role="img" aria-label="Large brushed metal disc decoration"></div>
    <div class="brand-lockup">
      <span class="brand-lockup__mark"></span>
    </div>
    <p class="company-name">
      <span><b style="font-weight:800">KLT</b></span>
      <span>Kerb Lane</span>
      <span class="company-name__strong">Traders</span>
    </p>
    <p class="tagline">Drive now, pay later</p>
  </section>
</body>
</html>
```